Summer Drinks Flyer for Coffee Shop

We are a coffee shop in London and would like to have a cool and nice flyer for our summer drinks (juices and frozen drink) flyer - see on the attached file for the list

Attached you can find an "attempt" - please note that I would no necessary need the image below.

I also attache our new logo.

thank you

Industry/Entity Type

Coffee Shop

```html
<!DOCTYPE html>
<html lang="en">
<head>
<meta charset="utf-8">
<title>New Summer Drinks Menu</title>
<link rel="stylesheet" href="https://fonts.googleapis.com/css2?family=Sniglet:wght@400;800&family=Delius&family=Arimo:wght@400&display=swap">
<style>
  :root {
    --backdrop: #3a3a3a;
    --sun-yellow: #f7c325;
    --sun-light: #fde79a;
    --cream: #fdf4dc;
    --sand: #f2dfae;
    --gold-band: #b8902a;
    --gold-text: #b8953a;
    --ink: #1c1c1c;
    --frame-silver: #c9c9c9;
    --photo-fill: #d9e6df;
  }
  * { margin: 0; padding: 0; box-sizing: border-box; }
  html, body { width: 913px; height: 1200px; overflow: hidden; background: var(--backdrop); }
  .canvas { position: relative; width: 913px; height: 1200px; }

  .flyer {
    position: absolute; left: 30px; top: 28px; width: 857px; height: 1144px;
    background: linear-gradient(180deg, var(--sun-yellow) 0%, #f9d34f 30%, var(--sun-light) 44%, var(--cream) 55%, #fbecc4 75%, var(--sand) 100%);
    overflow: hidden;
  }

  .photo-frame {
    position: absolute; left: 54px; top: 68px; width: 750px; height: 460px;
    background: linear-gradient(180deg, #eeeeee, var(--frame-silver));
    padding: 12px 13px 0 13px;
  }
  .photo-frame .photo {
    width: 100%; height: 100%;
    background: var(--photo-fill);
  }

  .title-band {
    position: absolute; left: 28px; top: 508px; width: 798px; height: 74px;
    background: linear-gradient(180deg, #c49a30, var(--gold-band));
    display: flex; align-items: center; justify-content: center;
  }
  .title-band h1 {
    font-family: "Sniglet", sans-serif; font-weight: 400; font-size: 44px;
    color: #fff; text-shadow: 2px 2px 3px rgba(0,0,0,0.45);
  }

  .menu { position: absolute; left: 40px; top: 668px; width: 760px; }
  .menu-item { margin-bottom: 20px; }
  .item-head {
    display: flex; align-items: baseline;
    font-family: "Delius", sans-serif; font-size: 24px; color: var(--ink);
    -webkit-text-stroke: 0.4px var(--ink);
  }
  .item-head .leader {
    flex: 1; border-bottom: 3px dotted #444; margin: 0 3px; transform: translateY(-3px);
  }
  .item-desc {
    font-family: "Arimo", sans-serif; font-size: 21px; line-height: 27px;
    color: var(--ink); text-align: center; margin: 0 -4px;
  }
  .item-desc small { font-size: 16px; }

  .footer {
    position: absolute; left: 20px; top: 1060px; width: 810px;
    display: flex; align-items: center; justify-content: space-between;
  }
  .brand { display: flex; align-items: center; gap: 10px; }
  .brand-dot { width: 18px; height: 18px; border-radius: 50%; background: var(--gold-text); }
  .brand-name {
    font-family: "Delius", sans-serif; font-size: 58px; color: var(--gold-text);
  }
  .contact {
    font-family: "Arimo", sans-serif; font-size: 48px; color: var(--ink);
  }
</style>
</head>
<body>
<div class="canvas">
  <div class="flyer">
    <div class="photo-frame">
      <div class="photo" role="img" aria-label="Photo of four tropical fruit drinks with garnishes"></div>
    </div>

    <div class="title-band"><h1>New Summer Drinks Menu</h1></div>

    <section class="menu">
      <div class="menu-item">
        <div class="item-head"><span>Frozen Fruit Drinks</span><span class="leader"></span><span>£2.95</span></div>
        <p class="item-desc">Strawberry and banana | Pineapple, mango and banana</p>
      </div>
      <div class="menu-item">
        <div class="item-head"><span>Fruit Juices</span><span class="leader"></span><span>£2.95</span></div>
        <p class="item-desc">Orange and carrot | Orange and pineapple | Pineapple and apple Apple and kiwi Carrot and ginger <small>(Add Mint or Ginger for Free!)</small></p>
      </div>
      <div class="menu-item">
        <div class="item-head"><span>Iced-Coffees</span><span class="leader"></span><span>£2.45</span></div>
        <p class="item-desc">Iced Coffee | Iced Latte | Iced Chocolate Drink <small>(Add Syrup shot for 10p)</small></p>
      </div>
    </section>

    <footer class="footer">
      <div class="brand"><span class="brand-dot"></span><span class="brand-name">Sorbella</span></div>
      <p class="contact">Your Contact info here</p>
    </footer>
  </div>
</div>
</body>
</html>
```